Company Employee Onboarding Presentation

We need a custom PowerPoint design for a company presentation. This presentation will be sent to new employees during their onboarding/hiring process. We have attached a current mock-up of the presentation - but this is for content only. We do not like the style of the mock-up. We're a commercial real estate investment company based in Los Angeles, CA. Our website is: www.thequillmrk.com.

One artistic element that we want in the presentation is that we want a timeline similar to the attached file, but want to overlay a rising bar chart from left to right that shows the total number of units owned rising through the years. We would like this to be in the background though by using a low opacity value for the color of the graph. A great example of what we want the timeline to look like is at the bottom of the following webpage (we would just need to add the rising bar chart in the background). https://www.tollmeridecap.com/firm. This timeline is what would take the place of page 4 of the attached PP presentation.

In addition to our company landing page, the following website is representative of a style we like: https://www.vak.com

```html
<!DOCTYPE html>
<html lang="en">
<head>
<meta charset="utf-8">
<title>The Quill Group – Onboarding Presentation</title>
<link rel="stylesheet" href="https://fonts.googleapis.com/css2?family=Poppins:wght@300;400;500;600;700;800&display=swap">
<style>
:root{
  --red:#d1232a;
  --ink:#1d1d1f;
  --body:#4a4a4a;
  --muted:#8a8a8a;
  --sheet:#e7e7e7;
  --panel:#f2f2f2;
  --line:#d9d9d9;
}
*{box-sizing:border-box;margin:0;padding:0}
html,body{width:1200px;height:3097px;overflow:hidden}
body{background:var(--sheet);font-family:"Poppins",sans-serif;color:var(--body);position:relative}
.slide{position:absolute;width:554px;height:310px;background:#fff;overflow:hidden}
.col-l{left:32px}.col-r{left:616px}
.photo{position:absolute}
.brand{position:absolute;font-family:"Poppins",sans-serif;font-weight:400;font-size:11px;color:#333;white-space:nowrap}
.brand.light{color:#fff}
.kicker{position:absolute;display:flex;align-items:center;font-weight:700;font-size:10.5px;color:var(--ink);white-space:nowrap}
.kicker::before{content:"";width:22px;height:7px;background:var(--red);margin-right:11px}
.kicker em{font-style:normal;color:var(--red)}
.kicker.light{color:#fff}
.txt{position:absolute;font-size:5.3px;line-height:1.42;color:var(--body)}
.txt p{margin-bottom:4px}
.txt b{color:var(--ink);font-weight:700}
.txt h4{font-size:5.6px;font-weight:700;color:var(--ink);margin-bottom:4px}
.option{position:absolute;font-size:17px;font-weight:300;color:#222;letter-spacing:.3px}
.card{position:absolute;background:#fff;box-shadow:0 1px 6px rgba(0,0,0,.12)}
.years{position:absolute;display:flex;justify-content:space-between;font-size:5.5px;color:#666}
.years .on{color:var(--red);font-weight:700}

/* cover */
.cover{left:322px;top:32px;width:555px;height:312px}
.cover .tag{position:absolute;left:188px;top:249px;border-left:1px solid #bbb;padding-left:11px}
.cover .tag span{display:block;font-size:12.5px;line-height:1.2}
.cover .tag .lead{color:var(--red);font-weight:300}
.cover .tag .main{color:var(--ink);font-weight:600}

/* business lines */
.line-card{position:absolute;top:90px;width:156px;height:198px;background:#fff;border-bottom:5px solid var(--red);padding:12px 10px}
.line-card .name{font-size:14px;font-weight:600;color:var(--ink);margin-bottom:8px;white-space:nowrap}
.line-card .txt{position:static;font-size:4.6px}

/* vertical timeline */
.vt-rail{position:absolute;left:102px;top:0;width:1px;height:310px;background:#bbb}
.vt-year{position:absolute;left:34px;font-size:9px;font-weight:700;color:var(--ink);display:flex;align-items:center}
.vt-year::after{content:"";width:14px;height:1px;background:#999;margin-left:6px}
.vt-dot{position:absolute;left:93px;width:19px;height:19px;border-radius:50%;border:1px solid var(--red);background:#fff}
.vt-dot::after{content:"";position:absolute;left:4px;top:4px;width:9px;height:9px;border-radius:50%;background:var(--red)}

/* stats */
.stat{position:absolute;width:110px;text-align:center}
.stat .ico{width:32px;height:32px;border-radius:50%;background:var(--red);margin:0 auto 5px;display:flex;align-items:center;justify-content:center}
.stat .num{font-size:10px;font-weight:600;color:var(--ink)}
.stat .lab{font-size:5.5px;color:#555;line-height:1.3}

/* values */
.values{position:absolute;left:246px;top:65px;list-style:none}
.values li{display:flex;align-items:center;height:19.6px;font-size:6.3px;color:#333}
.values li span{width:12px;height:12px;border-radius:50%;background:var(--red);color:#fff;font-size:6px;font-weight:600;display:flex;align-items:center;justify-content:center;margin-right:10px}
</style>
</head>
<body>

<!-- Cover -->
<section class="slide cover">
  <div class="photo" role="img" aria-label="White modern apartment buildings with trees and lawn" style="left:0;top:0;width:555px;height:232px;background:linear-gradient(180deg,#dfe6ec 0%,#eef1f2 45%,#9fae86 85%,#6c7f55 100%)"></div>
  <div class="brand" style="left:22px;top:250px;font-size:19px">The Quill Group</div>
  <div class="tag"><span class="lead">PROVIDING INNOVATIVE</span><span class="main">HOUSING SOLUTIONS NATIONWIDE.</span></div>
</section>

<!-- Who we are 1 -->
<section class="slide col-l" style="top:373px">
  <div class="photo" role="img" aria-label="Apartment tower balconies against a blue sky" style="inset:0;background:linear-gradient(120deg,#8fb3e8 0%,#c8dcf6 45%,#eef4fb 100%)"></div>
  <div class="photo" style="left:200px;top:115px;width:354px;height:85px;background:rgba(255,255,255,.82)"></div>
  <div class="kicker" style="left:270px;top:124px;margin-left:-33px">Who <em>&nbsp;We Are</em></div>
  <div class="brand" style="right:24px;top:122px">The Quill Group</div>
  <div class="txt" style="left:304px;top:150px;width:220px">The Quill Group develops and invests nationally in quality real estate projects across multiple business lines. We approach business through an entrepreneurial lens, cultivating a team who acts entrepreneurially and rewards team members commensurate with their contributions. This approach drives us to produce outsized returns.</div>
</section>

<!-- Who we are 2 -->
<section class="slide col-r" style="top:373px">
  <div class="photo" role="img" aria-label="Residential building with balconies and greenery" style="inset:0;background:linear-gradient(90deg,#c9c7bd 0%,#dcdad2 40%,#7f9a6a 100%)"></div>
  <div class="photo" style="left:272px;top:0;width:282px;height:310px;background:rgba(255,255,255,.88)"></div>
  <div class="kicker" style="left:272px;top:30px">Who <em>&nbsp;We Are</em></div>
  <div class="brand" style="right:22px;top:28px">The Quill Group</div>
  <div class="txt" style="left:306px;top:67px;width:228px">
    <p>While what we do determines our day-to-day, it's what we believe that makes us The Quill Group.</p>
    <p><b>We believe in being action oriented.</b> Results are achieved by compressing the distance between good ideas and great execution.</p>
    <p><b>We believe in authenticity.</b> It doesn't take a suit and tie to solve big problems. Work hard and be yourself.</p>
    <p><b>We believe in big goals.</b> In order to achieve uncommon results, our goals must push us out of our comfort zone, beyond what we think is possible.</p>
    <p><b>We believe we can do well while doing good.</b> We give back to our communities and aim to have a lasting social impact.</p>
    <p><b>We believe work and fun are not mutually exclusive.</b> When done right, hard work can be a lot of fun.</p>
    <p><b>We believe in a thoughtful approach.</b> We utilize our experience and a considered approach to make swift, reasoned and forward-thinking decisions.</p>
  </div>
</section>

<!-- Who we are 3 -->
<section class="slide col-l" style="top:713px">
  <div class="brand" style="left:34px;top:54px">The Quill Group</div>
  <div class="kicker" style="left:0;top:110px">Who <em>&nbsp;</em>We Are</div>
  <div class="txt" style="left:34px;top:133px;width:96px">The Quill Group develops and invests nationally in quality real estate projects across multiple business lines. We approach business through an entrepreneurial lens, cultivating a team who acts entrepreneurially and rewards team members commensurate with their contributions. This approach drives us to produce outsized returns.</div>
  <div class="photo" role="img" aria-label="Tall apartment tower balconies" style="left:157px;top:23px;width:123px;height:267px;background:linear-gradient(160deg,#d8e4f1,#9fb3c7 60%,#e9edf1)"></div>
  <div class="photo" role="img" aria-label="Resort pool with palm trees and lounge chairs" style="left:284px;top:23px;width:248px;height:133px;background:linear-gradient(180deg,#7fb1e4 0%,#c48d5c 55%,#5aa9c9 100%)"></div>
  <div class="photo" role="img" aria-label="Bright open lounge with orange chairs" style="left:284px;top:162px;width:121px;height:128px;background:linear-gradient(180deg,#f2f2f0,#cfcfcc 70%,#d9a26a)"></div>
  <div class="photo" role="img" aria-label="Residents cycling on a leafy path" style="left:411px;top:162px;width:121px;height:128px;background:linear-gradient(180deg,#a9c98a,#6f9a55 60%,#c9c6b3)"></div>
</section>

<!-- Business lines -->
<section class="slide col-r" style="top:713px;background:var(--panel)">
  <div class="photo" role="img" aria-label="Row of modern apartment buildings at dusk" style="left:0;top:0;width:554px;height:112px;background:linear-gradient(180deg,#4d6fa8 0%,#8a97ad 60%,#5a5e66 100%)"></div>
  <div class="kicker light" style="left:0;top:56px">Our Business Lines</div>
  <div class="brand" style="right:22px;top:47px">The Quill Group</div>
  <div class="line-card" style="left:30px">
    <div class="name">Quill Capital</div>
    <div class="txt"><p>Quill Capital is the Group's market rate investment vehicle founded on the basis of value investing philosophies, focusing on distressed, opportunistic, value-add and niche market real estate assets. Within these classes, we typically target underperforming properties that often require significant renovations and hands-on management to realize the assets' full potential.</p><p>Quill constantly assesses market conditions and end-user demand in order to identify short- and long-term inefficiencies and arbitrage opportunities. Subsequent to identifying a market opportunity, we apply a methodical approach to set the stage for realizing superior returns.</p></div>
  </div>
  <div class="line-card" style="left:199px">
    <div class="name">Quill Communities</div>
    <div class="txt"><p>In the context of a deepening affordability crisis, the Group entered affordable housing in 2013 with the establishment of Quill Communities, a developer, owner, and operator focused on providing affordable housing nationwide.</p><p>Through property-based Section 8 subsidies, Low Income Housing Tax Credits, and additional programs, we aim to preserve and expand long term housing affordability for low-income households. Our principals have a proven track record in the industry for safeguarding and growing the number of affordable units throughout the country.</p></div>
  </div>
  <div class="line-card" style="left:368px">
    <div class="name">Quill Impact Housing</div>
    <div class="txt"><p>Quill Impact Housing was founded to address the housing problem for middle income earners, individuals that cannot afford to reside in the communities in which they work.</p><p>Drawing upon the company's affordable and market-rate housing expertise, Impact Housing creates quality, income restricted housing units. The essential housing properties serve middle-income residents who earn incomes in excess of traditional affordable housing restrictions and yet cannot afford market rate housing without becoming rent burdened. The company undertakes these projects through strategic public-private partnerships with government agencies and financial institutions.</p></div>
  </div>
</section>

<div class="option" style="left:616px;top:1028px">OPTION 1</div>

<!-- Timeline with rising bars -->
<section class="slide col-l" style="top:1054px">
  <div class="kicker" style="left:0;top:30px">Company <em>&nbsp;History</em></div>
  <div class="brand" style="right:22px;top:29px">The Quill Group</div>
  <svg width="554" height="310" viewBox="0 0 554 310" style="position:absolute;left:0;top:0" font-family="Poppins, sans-serif">
    <rect x="0" y="120" width="554" height="57" fill="#f4f4f4"/>
    <g fill="#d1232a" opacity=".18">
      <rect x="110" y="168" width="16" height="9"/>
      <rect x="215" y="162" width="16" height="15"/>
      <rect x="268" y="153" width="16" height="24"/>
      <rect x="320" y="146" width="16" height="31"/>
      <rect x="372" y="140" width="16" height="37"/>
      <rect x="425" y="132" width="16" height="45"/>
      <rect x="478" y="124" width="16" height="53"/>
    </g>
    <g fill="#d1232a" opacity=".55">
      <rect x="215" y="162" width="16" height="15"/>
      <rect x="290" y="155" width="16" height="22"/>
      <rect x="376" y="148" width="16" height="29"/>
    </g>
    <g font-size="3.6" fill="#555" text-anchor="middle">
      <text x="223" y="157">2000+ Units</text><text x="298" y="150">4000+ Units</text><text x="384" y="143">5000+ Units</text>
    </g>
    <line x1="0" y1="177" x2="554" y2="177" stroke="#bbb" stroke-width=".8"/>
    <g font-size="5.5" fill="#555" text-anchor="middle">
      <text x="47" y="189">2010</text><text x="150" y="189">2013</text><text x="253" y="189">2016</text><text x="359" y="189">2019</text><text x="463" y="189">2022</text>
    </g>
    <g stroke="#d1232a" stroke-width=".6">
      <line x1="47" y1="80" x2="47" y2="130"/><line x1="90" y1="102" x2="90" y2="130"/><line x1="152" y1="80" x2="152" y2="130"/>
      <line x1="300" y1="102" x2="300" y2="130"/><line x1="330" y1="80" x2="330" y2="130"/><line x1="430" y1="80" x2="430" y2="130"/><line x1="470" y1="102" x2="470" y2="130"/>
      <line x1="65" y1="225" x2="65" y2="270"/><line x1="112" y1="225" x2="112" y2="252"/><line x1="210" y1="225" x2="210" y2="252"/><line x1="359" y1="225" x2="359" y2="252"/><line x1="440" y1="225" x2="440" y2="270"/>
    </g>
    <g font-size="3.8" fill="#555">
      <g fill="#d1232a" font-weight="600"><text x="50" y="80">Lorem ipsum</text><text x="93" y="102">Lorem ipsum</text><text x="155" y="80">Lorem ipsum</text><text x="303" y="102">Lorem ipsum</text><text x="333" y="80">Lorem ipsum</text><text x="433" y="80">Lorem ipsum</text><text x="473" y="102">Lorem ipsum</text>
      <text x="68" y="276">Lorem ipsum</text><text x="115" y="258">Lorem ipsum</text><text x="213" y="258">Lorem ipsum</text><text x="362" y="258">Lorem ipsum</text><text x="443" y="276">Lorem ipsum</text></g>
      <text x="50" y="86">Lorem ipsum dolor sit</text><text x="93" y="108">Lorem ipsum dolor sit</text><text x="155" y="86">Lorem ipsum dolor sit</text><text x="303" y="108">Lorem ipsum dolor sit</text><text x="333" y="86">Lorem ipsum dolor sit</text><text x="433" y="86">Lorem ipsum dolor sit</text><text x="473" y="108">Lorem ipsum dolor</text>
      <text x="68" y="282">Lorem ipsum dolor sit</text><text x="115" y="264">Lorem ipsum dolor sit</text><text x="213" y="264">Lorem ipsum dolor sit</text><text x="362" y="264">Lorem ipsum dolor sit</text><text x="443" y="282">Lorem ipsum dolor sit</text>
    </g>
    <g stroke="#fff" stroke-width="1.5">
      <circle cx="47" cy="138" r="12" fill="#6d9a55"/><circle cx="90" cy="138" r="12" fill="#8fb0d8"/><circle cx="152" cy="138" r="12" fill="#9a7a5a"/>
      <circle cx="300" cy="138" r="12" fill="#7b9a5a"/><circle cx="330" cy="138" r="12" fill="#b7c3cf"/><circle cx="430" cy="138" r="12" fill="#6b8a4f"/><circle cx="470" cy="138" r="12" fill="#a9bdd6"/>
      <circle cx="65" cy="214" r="12" fill="#b3b8be"/><circle cx="112" cy="214" r="12" fill="#7ea160"/><circle cx="210" cy="214" r="12" fill="#c9b19a"/><circle cx="359" cy="214" r="12" fill="#8fb4d4"/><circle cx="440" cy="214" r="12" fill="#6f8fbf"/>
    </g>
  </svg>
</section>

<!-- Option 1 -->
<section class="slide col-r" style="top:1054px;background:var(--panel)">
  <div class="photo" style="left:0;top:0;width:554px;height:68px;background:#fff"></div>
  <div class="kicker" style="left:0;top:30px">Company <em>&nbsp;History</em></div>
  <div class="brand" style="right:22px;top:29px">The Quill Group</div>
  <div class="card" style="left:22px;top:89px;width:246px;height:130px"></div>
  <div class="txt" style="left:50px;top:107px;width:200px"><h4>What do you get when you combine a principal, an unpaid intern, and 5,000 square feet of borrowed office space? The beginning of Quill.</h4><p>In 2010, we found the Company based on value investing principles in the depths of the Great Financial Crisis with a focus on value-add, distressed and opportunistic investments. We leave no stone unturned, using our experience and track record in the value-add institutional real estate investment space, starting small and building an investment firm from the ground up. It may not be the easiest path to choose, but <b>we do what's right and not what's easy.</b></p></div>
  <div class="card" style="left:283px;top:89px;width:246px;height:130px"></div>
  <div class="txt" style="left:311px;top:107px;width:200px"><h4>Start with what you know</h4><p>Finding a hidden gem, polishing it, and presenting it to the world can be a lot of fun. We know how to do it and enjoy doing it, so we decided to dive into the value-add apartment business. We find the worn out properties in great neighborhoods and we find the underutilized properties in the next hot neighborhoods. The key to success is to see things for what they can be, and not just what they are, then <b>to innovate through reimaging, reorganizing and reworking.</b></p></div>
  <div class="photo" style="left:22px;top:255px;width:510px;height:1px;background:#ccc"></div>
  <div class="photo" style="left:48px;top:251px;width:30px;height:10px;background:var(--red)"></div>
  <div class="years" style="left:52px;top:252px;width:458px"><span style="color:#fff;font-weight:600">2010</span><span>2011</span><span>2012</span><span>2013</span><span>2014</span><span>2015</span><span>2016</span><span>2017</span><span>2018</span><span>2019</span><span>2020</span><span>2021</span><span>2022</span></div>
</section>

<div class="option" style="left:32px;top:1368px">OPTION 2</div>
<div class="option" style="left:616px;top:1368px">OPTION 3</div>

<!-- Option 2 -->
<section class="slide col-l" style="top:1395px">
  <div class="photo" role="img" aria-label="Suburban apartment homes under a clear sky" style="left:0;top:0;width:554px;height:140px;background:linear-gradient(180deg,#6f86a6 0%,#9aa2a8 50%,#7c8a6c 100%)"></div>
  <div class="photo" style="left:0;top:0;width:554px;height:140px;background:rgba(30,30,30,.35)"></div>
  <div class="kicker light" style="left:0;top:30px">Company History</div>
  <div class="brand light" style="right:22px;top:29px">The Quill Group</div>
  <div class="card" style="left:90px;top:110px;width:407px;height:125px"></div>
  <div class="photo" style="left:84px;top:122px;width:68px;height:36px;background:var(--red);color:#fff;font-size:22px;font-weight:700;display:flex;align-items:center;justify-content:center">2011</div>
  <div class="txt" style="left:168px;top:140px;width:308px"><h4>Who wouldn't want to buy $1.00 for 70 cents?</h4><p>Armed with a man at the court house steps with an earpod in one ear and millions of dollars of cashier's checks in his back pocket, we embark on a daily ritual of bidding on apartment building foreclosures. Through the Stone Lantern Fund, a discretionary investment fund we raise to bid on foreclosed, distressed apartments, we successfully invest in this space over a four year period. With no traditional diligence available for the properties, and just seconds to bid, it can be a nerve wracking experience, but we never lose money on any of the acquisitions, and actually earn quite an attractive return. If this isn't a crash course in <b>making swift, reasoned and forward thinking decisions, we don't know what is.</b></p></div>
  <div class="photo" style="left:22px;top:279px;width:510px;height:1px;background:#ccc"></div>
  <div class="photo" style="left:22px;top:279px;width:110px;height:1px;background:var(--red)"></div>
  <div class="photo" style="left:130px;top:277px;width:5px;height:5px;border-radius:50%;background:var(--red)"></div>
  <div class="years" style="left:93px;top:268px;width:424px"><span>2010</span><span class="on">2011</span><span>2012</span><span>2013</span><span>2014</span><span>2015</span><span>2016</span><span>2017</span><span>2018</span><span>2019</span><span>2020</span><span>2021</span><span>2022</span></div>
</section>

<!-- Option 3 -->
<section class="slide col-r" style="top:1395px;background:var(--panel)">
  <div class="photo" style="left:0;top:0;width:554px;height:120px;background:#fff"></div>
  <div class="kicker" style="left:0;top:30px">Company <em>&nbsp;History</em></div>
  <div class="brand" style="right:22px;top:29px">The Quill Group</div>
  <svg width="554" height="30" viewBox="0 0 554 30" style="position:absolute;left:0;top:58px">
    <line x1="32" y1="13" x2="510" y2="13" stroke="#e3e3e3" stroke-width="6" stroke-linecap="round"/>
    <line x1="32" y1="13" x2="172" y2="13" stroke="#d1232a" stroke-width="6"/>
    <polygon points="32,5 46,13 32,21" fill="#111"/>
    <g fill="#fff" stroke="#333" stroke-width="1">
      <circle cx="68" cy="13" r="4"/><circle cx="103" cy="13" r="4"/><circle cx="137" cy="13" r="4"/><circle cx="172" cy="13" r="4"/><circle cx="207" cy="13" r="4"/><circle cx="242" cy="13" r="4"/><circle cx="277" cy="13" r="4"/><circle cx="312" cy="13" r="4"/><circle cx="347" cy="13" r="4"/><circle cx="382" cy="13" r="4"/><circle cx="417" cy="13" r="4"/><circle cx="452" cy="13" r="4"/><circle cx="487" cy="13" r="4"/>
    </g>
    <g fill="#333"><circle cx="68" cy="13" r="1.6"/><circle cx="103" cy="13" r="1.6"/><circle cx="137" cy="13" r="1.6"/><circle cx="172" cy="13" r="1.6"/><circle cx="207" cy="13" r="1.6"/><circle cx="242" cy="13" r="1.6"/><circle cx="277" cy="13" r="1.6"/><circle cx="312" cy="13" r="1.6"/><circle cx="347" cy="13" r="1.6"/><circle cx="382" cy="13" r="1.6"/><circle cx="417" cy="13" r="1.6"/><circle cx="452" cy="13" r="1.6"/><circle cx="487" cy="13" r="1.6"/></g>
  </svg>
  <div class="years" style="left:58px;top:90px;width:440px"><span>2010</span><span>2011</span><span class="on">2012</span><span class="on">2013</span><span>2014</span><span>2015</span><span>2016</span><span>2017</span><span>2018</span><span>2019</span><span>2020</span><span>2021</span><span>2022</span></div>
  <div class="card" style="left:22px;top:148px;width:246px;height:130px"></div>
  <div class="txt" style="left:50px;top:168px;width:200px"><h4>Eureka!</h4><p>After a nail biting 22 months of money going out the door during the Company's initial existence, we successfully complete our first disposition of an investment which (thankfully) brings some profit back into the bank account. With a sale price 55% above our purchase, we're off to a good start. And better yet, our investment thesis is validated.</p></div>
  <div class="card" style="left:283px;top:148px;width:246px;height:130px"></div>
  <div class="txt" style="left:311px;top:168px;width:200px"><h4>Doing well while doing good.</h4><p>After rigorous analysis we dip our toe in the affordable housing waters because of perceived opportunity. While the initial opportunity is just a sliver of the vast affordable housing landscape we uncover in the years to come, the affordable housing business becomes more of a mission rather than just a mere opportunity. We create a new segment of the business, Quill Communities, to focus on fulfilling affordable housing needs across the country. This would not be possible without our pursuit of lifelong learning, allowing us to marry our existing multifamily experience with a new asset class.</p></div>
</section>

<div class="option" style="left:32px;top:1710px">OPTION 4</div>

<!-- Option 4a -->
<section class="slide col-l" style="top:1735px">
  <div class="vt-rail"></div>
  <div class="kicker" style="left:164px;top:32px">Company <em>&nbsp;History</em></div>
  <div class="brand" style="right:22px;top:31px">The Quill Group</div>
  <div class="vt-year" style="top:68px">2015</div><div class="vt-dot" style="top:66px"></div>
  <div class="vt-year" style="top:149px">2016</div><div class="vt-dot" style="top:147px"></div>
  <div class="vt-year" style="top:229px">2017</div><div class="vt-dot" style="top:227px"></div>
  <div class="txt" style="left:164px;top:72px;width:222px"><h4>The Open Quarter</h4><p>Just off the glittering Sun Valley strip we find what we believe to be an attractive affordable housing opportunity. But once we complete our diligence, we realize that the property has too many physical needs to be a viable long term investment. Rather than walking away, we decide to dive deeper into the affordable housing world by utilizing the Low Income Housing Tax Credit to complete a redevelopment of the 201 unit property located in a neighborhood known as The Open Quarter. This redevelopment not only enhances the lives of the property's residents, but contributes to lifting the entire neighborhood. This is the first of many projects Quill Communities undertakes to redevelop affordable housing across the country.</p></div>
  <div class="txt" style="left:164px;top:216px;width:222px"><h4>Ladies and gentlemen, start your engines.</h4><p>While the debate still rages in the office as to who actually won the inaugural Quill go karting race, one thing is certain: we all walk away that day with big smiles on our faces. <b>We work hard and have fun, otherwise, what's the point?</b></p></div>
</section>

<!-- Option 4b -->
<section class="slide col-r" style="top:1735px">
  <div class="vt-rail"></div>
  <div class="kicker" style="left:164px;top:32px">Company <em>&nbsp;History</em></div>
  <div class="brand" style="right:22px;top:31px">The Quill Group</div>
  <div class="vt-year" style="top:68px">2019</div><div class="vt-dot" style="top:66px"></div>
  <div class="vt-year" style="top:149px">2020</div><div class="vt-dot" style="top:147px"></div>
  <div class="vt-year" style="top:229px">2021</div><div class="vt-dot" style="top:227px"></div>
  <div class="txt" style="left:164px;top:72px;width:222px"><h4>46..., 47..., 48..., 49..., 50!</h4><p>Never are we met with such a range of emotions for a company activity: excitement, nervousness, dread. The Quill health challenge is a 60 day competition that tests our willpower, establishes beneficial habits, and leaves us feeling a better version of ourselves. We gain points by simply eating right and working out, all while having a trainer cheering us along or giving us a nudge. Our single biggest competitor is ourself. To be successful, <b>we must approach each day with intention</b>, just like we approach our business. A testament to the spirit of the team, the competition is neck and neck until the very end.</p></div>
  <div class="txt" style="left:164px;top:176px;width:222px"><h4>Solving for the missing middle</h4><p>How can we have thriving cities when the people who work and play there cannot afford to live there? Spoiler alert: we can't. Expensive, high-end housing pencils to build. Affordable housing for low income renters, although scarce, can pencil to build through government funded programs. But what about middle income renters who make the cities run? They are left with dilapidated, old housing stock, or spending hours a day fighting traffic to get to and from work. <b>Harnessing the collective and collaborative power of a public/private team</b>, Quill Impact Housing is born to address this crucial need, providing high quality housing to the teachers, nurses, and numerous professionals who are the life blood of our cities.</p></div>
</section>

<!-- Option 4c -->
<section class="slide col-l" style="top:2075px">
  <div class="vt-rail"></div>
  <div class="kicker" style="left:164px;top:32px">Company <em>&nbsp;History</em></div>
  <div class="brand" style="right:22px;top:31px">The Quill Group</div>
  <div class="vt-year" style="top:78px">2021</div><div class="vt-dot" style="top:76px"></div>
  <div class="vt-year" style="top:162px">2022</div><div class="vt-dot" style="top:160px"></div>
  <div class="txt" style="left:164px;top:82px;width:222px"><h4>Movin' on up</h4><p>The growth and success of a company does not happen overnight, nor does it just happen. It takes a team of dedicated, intelligent, results oriented individuals to deliver exceptional results. When a member of the team consistently delivers results, <b>we reward those results.</b> In this case, we name our first Partner.</p></div>
  <div class="txt" style="left:164px;top:164px;width:222px"><h4>Don't step in the kitchen</h4><p>What company retreat is complete without a bit of work, a lot of laughs, and little competition? The competitive juices are in full swing at the first Quill pickleball tournament. The open courtside bar soothes the sting of defeat, but regardless of where we each rank in the standings, there is a lot of talk of pickleball becoming the new favorite Quill pastime.</p></div>
</section>

<!-- Where we are now -->
<section class="slide col-r" style="top:2075px">
  <div class="photo" role="img" aria-label="Colorful apartment complex with landscaped courtyard" style="left:0;top:0;width:212px;height:310px;background:linear-gradient(180deg,#a9c3de 0%,#c9a27a 35%,#8a6f55 60%,#5f7f4a 100%)"></div>
  <div class="kicker" style="left:212px;top:30px;margin-left:-33px;padding-left:0"><span style="margin-left:0">Where Are We <em>Now</em></span></div>
  <div class="brand" style="right:22px;top:31px">The Quill Group</div>
  <div class="stat" style="left:228px;top:90px"><div class="ico"><svg width="14" height="14" viewBox="0 0 14 14" fill="#fff"><rect x="2" y="2" width="10" height="12"/><g fill="#d1232a"><rect x="4" y="4" width="2" height="2"/><rect x="8" y="4" width="2" height="2"/><rect x="4" y="8" width="2" height="2"/><rect x="8" y="8" width="2" height="2"/></g></svg></div><div class="num">7,500+</div><div class="lab">Apartment Units<br>Acquired</div></div>
  <div class="stat" style="left:337px;top:90px"><div class="ico"><svg width="16" height="14" viewBox="0 0 16 14" fill="#fff"><circle cx="4" cy="4" r="2"/><circle cx="8" cy="3" r="2"/><circle cx="12" cy="4" r="2"/><rect x="1" y="8" width="14" height="4" rx="1"/></svg></div><div class="num">Over $4 billion</div><div class="lab">Senior Management Team<br>Acquisition Experience</div></div>
  <div class="stat" style="left:442px;top:90px"><div class="ico"><svg width="12" height="14" viewBox="0 0 12 14" fill="none" stroke="#fff" stroke-width="1.4"><rect x="1" y="1" width="10" height="12"/><line x1="3" y1="5" x2="9" y2="5"/><line x1="3" y1="8" x2="9" y2="8"/></svg></div><div class="num">$1+ billion</div><div class="lab">Current Assets<br>Under Management</div></div>
  <div class="stat" style="left:228px;top:182px"><div class="ico"><svg width="16" height="12" viewBox="0 0 16 12" fill="#fff"><rect x="0" y="0" width="16" height="3"/><rect x="2" y="3" width="2" height="7"/><rect x="6" y="3" width="2" height="7"/><rect x="10" y="3" width="2" height="7"/><rect x="0" y="10" width="16" height="2"/></svg></div><div class="num">13,000+</div><div class="lab">Number of Residents<br>Served</div></div>
  <div class="stat" style="left:337px;top:182px"><div class="ico"><svg width="12" height="14" viewBox="0 0 12 14" fill="#fff"><circle cx="6" cy="4" r="3"/><rect x="2" y="8" width="8" height="6"/></svg></div><div class="num">$60mm+</div><div class="lab">Renovations<br>Performed</div></div>
  <div class="stat" style="left:442px;top:182px"><div class="ico"><svg width="14" height="12" viewBox="0 0 14 12" fill="none" stroke="#fff" stroke-width="1.4"><polyline points="1,11 5,6 8,8 13,2"/><line x1="1" y1="11" x2="13" y2="11"/></svg></div><div class="num">34.87%</div><div class="lab">IRR of Realized<br>Investments – Quill<br>Communities</div></div>
</section>

<!-- Portfolio -->
<section class="slide col-l" style="top:2416px">
  <div class="kicker" style="left:0;top:32px">Our Nationwide <em>&nbsp;Portfolio</em></div>
  <div class="brand" style="right:22px;top:31px">The Quill Group</div>
  <div class="txt" style="left:34px;top:120px;width:185px"><h4>Lorem ipsum dolor sit amet, consectetuer</h4><p>Lorem ipsum dolor sit amet, consectetuer adipiscing elit, sed diam nonummy nibh euismod tincidunt ut laoreet dolore magna aliquam erat volutpat. Ut wisi enim ad minim veniam, quis nostrud exerci tation ullamcorper suscipit lobortis nisl ut aliquip ex ea commodo consequat. Duis autem vel eum iriure dolor in hendrerit in vulputate velit esse molestie consequat, vel illum dolore eu feugiat nulla facilisis at vero eros et accumsan et iusto odio dignissim qui blandit praesent luptatum zzril delenit augue duis dolore te feugait nulla facilisi.</p></div>
  <div class="photo" role="img" aria-label="Map of the United States with portfolio states highlighted in red" style="left:250px;top:97px;width:276px;height:138px;background:linear-gradient(90deg,#c9c9c9 0%,#d1232a 30%,#c9c9c9 55%,#d1232a 85%,#c9c9c9 100%);opacity:.85;border-radius:6px"></div>
</section>

<!-- Tomorrow -->
<section class="slide col-r" style="top:2416px">
  <div class="photo" role="img" aria-label="Modern white apartment building with balconies" style="inset:0;background:linear-gradient(90deg,#e6e8ea 0%,#bfc5cb 45%,#dfe3e6 100%)"></div>
  <div class="photo" style="left:270px;top:0;width:284px;height:310px;background:rgba(255,255,255,.88)"></div>
  <div class="kicker" style="left:270px;top:30px;margin-left:-33px">What Does</div>
  <div style="position:absolute;left:306px;top:44px;font-size:10.5px;font-weight:700;color:var(--red)">Tomorrow Look Like?</div>
  <div class="brand" style="right:22px;top:29px">The Quill Group</div>
  <div class="txt" style="left:306px;top:68px;width:228px">
    <p><b>We will be a market leader.</b> We will pursue growth and innovation to achieve industry beating returns and exponentially expand our portfolio through new and existing business lines.</p>
    <p><b>We will positively impact those we touch.</b> We have a responsibility to create opportunity for our residents and our employees. Investing in the communities where we live and work, we will help us enact the social impact that is sorely needed.</p>
    <p><b>We will have a positive impact on those we touch.</b> We will positively impact all stakeholders in our business (residents, employees, communities and investors) by adhering to a high standard in terms of both our fiduciary and social obligations.</p>
    <p><b>We will have a positive and lasting effect on residents/communities by doing what's right not what's easy.</b></p>
    <p><b>We will reduce our footprint.</b> We recognize that the construction industry has a significant carbon footprint. Through our perpetual desire to innovate through reimagining, reorganizing and reworking, we will find further solutions to substantially reduce the carbon footprint of our communities.</p>
    <p><b>We will utilize our expertise to its fullest.</b> The multifamily industry has been one of the highest performing asset classes, and is poised to remain such. We will outperform the already favorable market by applying all of our experience to mitigate risk and enhance upside.</p>
  </div>
</section>

<!-- Core values -->
<section class="slide col-l" style="top:2756px">
  <div class="photo" role="img" aria-label="Volunteers planting in a community garden" style="left:84px;top:0;width:136px;height:310px;background:linear-gradient(180deg,#3f5a34 0%,#6e8a4f 45%,#2f3f2a 100%)"></div>
  <div style="position:absolute;left:40px;top:110px;width:88px;height:88px;border-radius:50%;background:var(--red);color:#fff;font-size:10.5px;font-weight:700;line-height:1.2;display:flex;align-items:center;justify-content:center;text-align:center">Our Core<br>Values</div>
  <div class="brand" style="right:22px;top:36px">The Quill Group</div>
  <ol class="values">
    <li><span>1</span>We do what's right, not what's easy</li>
    <li><span>2</span>We lead by example</li>
    <li><span>3</span>We harness the collective and collaborative power of the team</li>
    <li><span>4</span>We empower individuals</li>
    <li><span>5</span>We make swift, reasoned and forward-thinking decisions</li>
    <li><span>6</span>We pursue lifelong learning</li>
    <li><span>7</span>We reward results</li>
    <li><span>8</span>We approach each day with intention</li>
    <li><span>9</span>We innovate through reimagining, reorganizing and reworking</li>
    <li><span>10</span>We think and act like owners</li>
    <li><span>11</span>We work hard and have fun</li>
  </ol>
</section>

<!-- Thank you -->
<section class="slide col-r" style="top:2756px">
  <div class="photo" role="img" aria-label="Apartment buildings at dusk" style="inset:0;background:linear-gradient(180deg,#3a3d42 0%,#55585c 50%,#2b2d30 100%)"></div>
  <div class="brand light" style="left:0;right:0;top:112px;text-align:center;font-size:17px">The Quill Group</div>
  <div style="position:absolute;left:0;right:0;top:138px;text-align:center;color:#fff;font-size:28px;font-weight:700;letter-spacing:.5px">THANK YOU!</div>
  <div style="position:absolute;left:250px;top:182px;display:flex;gap:7px">
    <span style="width:15px;height:15px;border-radius:50%;background:var(--red)"></span>
    <span style="width:15px;height:15px;border-radius:50%;background:var(--red)"></span>
    <span style="width:15px;height:15px;border-radius:50%;background:var(--red)"></span>
  </div>
</section>

</body>
</html>
```